Newsletter for customers of the IT company

Our company develops the software.
We need to create a monthly newsletter for our customers. The newsletter is distributed by email. Important points to follow:
1/ Newsletter has to include the logo and link to ProfilNet profile of company - https://www.profilnet.example/company/vorek-software-cz/?viewAsMember=true
2/ Corporate color is RGB #003265, you can use it.
3/ Use the most used fonts (calibri, times, trebuchet, verdana, ubuntu etc.).
4/ We need it in the html in final version.
5/ We would like to highlight the offer of webinars (3-4 per month).
6/ There have to be the space for news from company (2-3 per month) and link to website with news in the version of software.
7/ Space for contact.

```html
<!DOCTYPE html>
<html lang="en">
<head>
<meta charset="utf-8">
<title>VOREK – Monthly Newsletter</title>
<link href="https://fonts.googleapis.com/css2?family=Carlito:wght@400;700&family=Open+Sans:wght@400;600;700&display=swap" rel="stylesheet">
<style>
  :root {
    --brand: #003265;
    --brand-mid: #0a4484;
    --brand-dark: #002a56;
    --white: #ffffff;
    --ink: #111111;
    --text: #333333;
    --hero-a: #2b2f36;
    --hero-b: #151a22;
    --social: #1a8ad1;
  }
  * { margin: 0; padding: 0; box-sizing: border-box; }
  html, body { width: 1200px; height: 5162px; overflow: hidden; }
  body { position: relative; background: var(--white); font-family: "Carlito", "Calibri", sans-serif; color: var(--ink); }
  a { color: inherit; }
  .abs { position: absolute; }

  /* Hero */
  .hero { left: 0; top: 0; width: 1200px; height: 1194px; background: linear-gradient(135deg, var(--hero-a), var(--hero-b)); }
  .brand-box { left: 414px; top: 0; width: 368px; height: 294px; background: var(--white); display: flex; align-items: center; justify-content: center; }
  .brand-name { font-family: "Open Sans", sans-serif; font-weight: 700; font-size: 58px; color: var(--brand); letter-spacing: 2px; }
  .hero-line { left: 0; width: 1200px; text-align: center; font-family: "Open Sans", sans-serif; color: var(--white); }
  .hero-top { top: 480px; font-size: 96px; font-weight: 600; letter-spacing: 12px; line-height: 1; }
  .hero-outline { top: 578px; font-size: 184px; font-weight: 400; letter-spacing: 14px; line-height: 1; color: transparent; -webkit-text-stroke: 3px var(--white); }
  .hero-bottom { top: 748px; font-size: 96px; font-weight: 700; letter-spacing: 12px; line-height: 1; }
  .hero-social { left: 0; top: 866px; width: 1200px; display: flex; justify-content: center; align-items: center; gap: 14px; color: var(--white); font-size: 30px; text-decoration: none; }
  .dot { display: inline-block; width: 56px; height: 56px; border-radius: 50%; background: var(--social); }

  /* Webinars */
  .section-title { left: 0; width: 1200px; text-align: center; font-weight: 700; font-size: 96px; line-height: 1; color: var(--ink); }
  .webinars-title { top: 1304px; }
  .webinar-date { left: 0; top: 1450px; width: 1200px; text-align: center; font-size: 35px; line-height: 46px; color: var(--brand); }
  .btn { left: 434px; top: 1574px; width: 330px; height: 66px; border-radius: 33px; background: var(--brand); color: var(--white); font-size: 27px; display: flex; align-items: center; justify-content: center; text-decoration: none; }

  .webinar { left: 0; width: 1200px; height: 560px; }
  .webinar-1 { top: 1764px; background: var(--brand); }
  .webinar-2 { top: 2324px; background: var(--brand-mid); }
  .webinar-3 { top: 2884px; background: var(--brand); }
  .speaker-photo { background: linear-gradient(180deg, #4a6ea3 0%, #1f2a3a 100%); }
  .speaker-1 { left: 66px; top: 1704px; width: 470px; height: 620px; }
  .speaker-2 { left: 690px; top: 2152px; width: 390px; height: 732px; }
  .speaker-3 { left: 92px; top: 2784px; width: 500px; height: 660px; }
  .webinar-text { color: var(--white); }
  .webinar-name { font-size: 74px; line-height: 84px; }
  .webinar-time { font-size: 37px; margin-top: 6px; }
  .webinar-more { display: inline-block; font-size: 22px; margin-top: 20px; text-decoration: underline; }
  .text-1 { left: 640px; top: 1880px; }
  .text-2 { left: 100px; top: 2458px; }
  .text-3 { left: 640px; top: 3020px; }

  /* News */
  .news-title { top: 3560px; }
  .news-card { top: 3724px; width: 476px; height: 676px; background: var(--white); box-shadow: 0 20px 50px rgba(0,0,0,0.12); }
  .card-1 { left: 106px; }
  .card-2 { left: 618px; }
  .news-photo { width: 476px; height: 366px; }
  .photo-hall { background: linear-gradient(180deg, #b68a3c 0%, #6b4a2a 50%, #2c2f52 100%); }
  .photo-stage { background: linear-gradient(180deg, #c9b2e6 0%, #e9e6f0 55%, #4a4a5c 100%); }
  .news-body { padding: 26px 56px 0; }
  .news-author { display: flex; align-items: center; gap: 8px; font-size: 20px; color: var(--brand); }
  .news-heading { font-size: 34px; font-weight: 700; margin-top: 10px; color: var(--ink); }
  .news-excerpt { font-size: 20px; line-height: 30px; margin-top: 10px; color: var(--text); }
  .news-link { display: inline-flex; align-items: center; gap: 10px; margin-top: 16px; font-size: 28px; color: var(--brand); }
  .news-link span { text-decoration: underline; }

  /* Contact */
  .contact { left: 0; top: 4514px; width: 1200px; height: 648px; background: var(--brand); color: var(--white); }
  .contact-title { left: 0; top: 100px; width: 1200px; text-align: center; font-size: 68px; font-weight: 700; }
  .contact-details { left: 104px; top: 284px; font-size: 34px; line-height: 36px; }
  .contact-details p { margin-bottom: 42px; }
  .follow { right: 104px; top: 280px; text-align: right; }
  .follow-title { font-size: 42px; font-weight: 700; }
  .follow-link { display: inline-flex; align-items: center; gap: 12px; margin-top: 22px; font-size: 26px; text-decoration: none; }
  .legal { margin-top: 22px; font-size: 20px; }
  .legal a { text-decoration: none; }
</style>
</head>
<body>

<header>
  <div class="abs hero" role="img" aria-label="Photo of developers working at computers with code on screen"></div>
  <div class="abs brand-box"><span class="brand-name">VOREK</span></div>
  <div class="abs hero-line hero-top">OUR COMPANY</div>
  <div class="abs hero-line hero-outline">DEVELOPS</div>
  <div class="abs hero-line hero-bottom">THE SOFTWARE</div>
  <a class="abs hero-social" href="https://www.profilnet.example/company/vorek-software-cz/?viewAsMember=true"><span class="dot"></span>ProfilNet</a>
</header>

<section>
  <h2 class="abs section-title webinars-title">Webinars</h2>
  <p class="abs webinar-date">Tuesday, Jan 2<br>at 12:00 pm in the lobby</p>
  <a class="abs btn" href="#">Join Now</a>

  <div class="abs webinar webinar-1"></div>
  <div class="abs speaker-photo speaker-1" role="img" aria-label="Speaker in suit and glasses, hands on hips"></div>
  <div class="abs webinar-text text-1">
    <div class="webinar-name">Digital Think<br>Meet Up</div>
    <div class="webinar-time">9.30 - 10.30 AM Workshop</div>
    <a class="webinar-more" href="#">Read More</a>
  </div>

  <div class="abs webinar webinar-2"></div>
  <div class="abs speaker-photo speaker-2" role="img" aria-label="Speaker in suit holding a microphone"></div>
  <div class="abs webinar-text text-2">
    <div class="webinar-name">Digital Think<br>Meet Up</div>
    <div class="webinar-time">9.30 - 10.30 AM Workshop</div>
    <a class="webinar-more" href="#">Read More</a>
  </div>

  <div class="abs webinar webinar-3"></div>
  <div class="abs speaker-photo speaker-3" role="img" aria-label="Speaker in dark blazer with arms crossed"></div>
  <div class="abs webinar-text text-3">
    <div class="webinar-name">Digital Think<br>Meet Up</div>
    <div class="webinar-time">9.30 - 10.30 AM Workshop</div>
    <a class="webinar-more" href="#">Read More</a>
  </div>
</section>

<section>
  <h2 class="abs section-title news-title">Latest News</h2>

  <article class="abs news-card card-1">
    <div class="news-photo photo-hall" role="img" aria-label="Conference hall with delegates seated at desks"></div>
    <div class="news-body">
      <div class="news-author">
        <svg width="26" height="26" viewBox="0 0 24 24"><circle cx="12" cy="7" r="5" fill="#003265"/><path d="M2 24c0-6 4.5-10 10-10s10 4 10 10z" fill="#003265"/></svg>
        by Vorek
      </div>
      <h3 class="news-heading">Proin fermentum</h3>
      <p class="news-excerpt">Sed ultricies ut justo et bibendum. Sed massa lacus, placerat vel elit vel, consequat auctor lacus.</p>
      <a class="news-link" href="#"><span>Continue</span>
        <svg width="32" height="22" viewBox="0 0 32 22"><path d="M2 11h26M19 3l9 8-9 8" fill="none" stroke="#003265" stroke-width="3.5"/></svg>
      </a>
    </div>
  </article>

  <article class="abs news-card card-2">
    <div class="news-photo photo-stage" role="img" aria-label="Event stage with audience and camera crew"></div>
    <div class="news-body">
      <div class="news-author">
        <svg width="26" height="26" viewBox="0 0 24 24"><circle cx="12" cy="7" r="5" fill="#003265"/><path d="M2 24c0-6 4.5-10 10-10s10 4 10 10z" fill="#003265"/></svg>
        by Vorek
      </div>
      <h3 class="news-heading">Proin fermentum</h3>
      <p class="news-excerpt">Sed ultricies ut justo et bibendum. Sed massa lacus, placerat vel elit vel, consequat auctor lacus.</p>
      <a class="news-link" href="#"><span>Continue</span>
        <svg width="32" height="22" viewBox="0 0 32 22"><path d="M2 11h26M19 3l9 8-9 8" fill="none" stroke="#003265" stroke-width="3.5"/></svg>
      </a>
    </div>
  </article>
</section>

<footer class="abs contact">
  <h2 class="abs contact-title">Contact Us</h2>
  <div class="abs contact-details">
    <p>4410 Harlow Street, Cedar Vale,<br>CA 90210.</p>
    <p>123-555-01890</p>
    <p>info@vorekmail.example</p>
  </div>
  <div class="abs follow">
    <div class="follow-title">Follow Us On</div>
    <a class="follow-link" href="https://www.profilnet.example/company/vorek-software-cz/?viewAsMember=true"><span class="dot"></span>ProfilNet</a>
    <div class="legal"><a href="#">Privacy Policy</a> &nbsp;|&nbsp; <a href="#">Terms &amp; Conditions</a></div>
  </div>
</footer>

</body>
</html>
```